Logo and business card design

I would like a logo and business card designed for a bookkeeping business called "Brightwell Accounting"
Would like the submission to be an editable file.

Info for business card:

Mara Lint, CPA, CGA
President
maralint@mailbox.example
555.301.8842
Toronto, ON

```html
<!DOCTYPE html>
<html lang="en">
<head>
<meta charset="utf-8">
<title>Brightwell Accounting – Business Card</title>
<link rel="stylesheet" href="https://fonts.googleapis.com/css2?family=Montserrat:wght@400;500;700&display=swap">
<style>
  :root {
    --purple: #7d1d8c;
    --orange: #f08a12;
    --ink: #2b2b2b;
    --card: #ffffff;
    --backdrop: #3a3a3c;
  }
  * { box-sizing: border-box; margin: 0; padding: 0; }
  html, body {
    width: 1200px; height: 920px; overflow: hidden;
    background: var(--backdrop);
    font-family: "Montserrat", Arial, sans-serif;
  }
  .stage { position: relative; width: 1200px; height: 920px; }
  .card {
    position: absolute;
    width: 620px; height: 354px;
    background: var(--card);
    border-radius: 4px;
    box-shadow: 0 10px 24px rgba(0,0,0,.35);
    overflow: hidden;
  }
  .card--front { left: 110px; top: 70px; }
  .card--back  { left: 470px; top: 496px; }

  .wordmark {
    display: flex; align-items: center; gap: 14px;
    color: var(--purple); font-weight: 700;
  }
  .wordmark__square { background: var(--orange); flex: none; }
  .card--front .wordmark {
    position: absolute; left: 0; right: 0; top: 0; bottom: 0;
    justify-content: center; font-size: 40px;
  }
  .card--front .wordmark__square { width: 34px; height: 34px; }

  .card--back .wordmark {
    position: absolute; left: 32px; top: 150px; width: 220px;
    font-size: 24px; line-height: 1.15;
  }
  .card--back .wordmark__square { width: 22px; height: 22px; }

  .divider {
    position: absolute; left: 268px; top: 70px;
    width: 2px; height: 200px; background: var(--purple);
  }
  .contact {
    position: absolute; left: 288px; right: 20px; top: 66px;
    color: var(--ink); font-size: 15px; line-height: 1.35;
  }
  .contact__name { color: var(--purple); font-weight: 700; font-size: 20px; }
  .contact__title { font-size: 14px; margin-bottom: 10px; }
  .contact__row { display: flex; gap: 10px; align-items: center; margin-bottom: 8px; }
  .contact__icon {
    width: 30px; height: 30px; background: var(--purple);
    display: flex; align-items: center; justify-content: center; flex: none;
  }
  .contact__web { color: var(--purple); }
  .contact__city { margin-top: 4px; }
</style>
</head>
<body>
<div class="stage">
  <section class="card card--front">
    <div class="wordmark">
      <span class="wordmark__square"></span>
      <span>Brightwell Accounting</span>
    </div>
  </section>

  <section class="card card--back">
    <div class="wordmark">
      <span class="wordmark__square"></span>
      <span>Brightwell Accounting</span>
    </div>
    <div class="divider"></div>
    <div class="contact">
      <p class="contact__name">MARA LINT, CPA, CGA</p>
      <p class="contact__title">President</p>
      <div class="contact__row">
        <span class="contact__icon">
          <svg width="18" height="18" viewBox="0 0 24 24" aria-hidden="true">
            <path fill="#fff" d="M6.6 10.8a15.1 15.1 0 0 0 6.6 6.6l2.2-2.2c.3-.3.7-.4 1-.2 1.1.4 2.3.6 3.6.6.6 0 1 .4 1 1V20c0 .6-.4 1-1 1A17 17 0 0 1 3 4c0-.6.4-1 1-1h3.5c.6 0 1 .4 1 1 0 1.3.2 2.5.6 3.6.1.3 0 .7-.2 1z"/>
          </svg>
        </span>
        <div><p>555.301.8842</p><p>555.301.8843</p></div>
      </div>
      <div class="contact__row">
        <span class="contact__icon">
          <svg width="18" height="18" viewBox="0 0 24 24" aria-hidden="true" fill="none" stroke="#fff" stroke-width="1.6">
            <circle cx="12" cy="12" r="9"/>
            <ellipse cx="12" cy="12" rx="4" ry="9"/>
            <path d="M3 12h18M5 7h14M5 17h14"/>
          </svg>
        </span>
        <div><p>maralint@mailbox.example</p><p class="contact__web">www.brightwell.example</p></div>
      </div>
      <p class="contact__city">Toronto, ON. Canada.</p>
    </div>
  </section>
</div>
</body>
</html>
```